Design our next "COPPER VALLEY" print. Size 12x36 Horizontal.

I am looking for a poster design with the text "Copper Valley" . The print size will be a 12x36 inches.(Horizontal) It should have the American flag used throughout the design. I am looking for a very proud feeling. Font can be creative but instantly readable. The design can be old world feel and can also use the deep reds and navy blues.The image does not have to be just the flag and text. It can contain other patriotic symbols. Can also have a grungy feel. I have enclosed our last "Copper Valley " piece for your reference. We are hoping we can get one even better. Thank You.

• Should Not be like the image example I enclosed. It's just a reference. We need something that is new and different. Plain White text.

```html
<!DOCTYPE html>
<html lang="en">
<head>
<meta charset="utf-8">
<title>Copper Valley Print</title>
<link rel="stylesheet" href="https://fonts.googleapis.com/css2?family=Alfa+Slab+One&display=swap">
<style>
  :root {
    --page-bg: #2a2a2c;
    --sky-blue: #7fb6c9;
    --steel-blue: #6e93b4;
    --navy: #3b4f86;
    --flag-red: #b8392f;
    --flag-white: #e6e2dc;
    --title-red: #e2302c;
    --title-blue: #1f4fa8;
    --shadow: rgba(10, 20, 40, 0.55);
  }
  html, body {
    margin: 0;
    padding: 0;
    width: 1125px;
    height: 1200px;
    overflow: hidden;
    background: var(--page-bg);
  }
  .canvas {
    position: relative;
    width: 1125px;
    height: 1200px;
  }
  .print {
    position: absolute;
    left: 30px;
    top: 422px;
    width: 1065px;
    height: 355px;
    overflow: hidden;
  }
  .flag-artwork {
    position: absolute;
    inset: 0;
    background:
      linear-gradient(90deg,
        var(--sky-blue) 0%,
        var(--steel-blue) 28%,
        var(--navy) 50%,
        var(--navy) 59%,
        rgba(184, 57, 47, 0) 59.5%),
      repeating-linear-gradient(180deg,
        var(--flag-white) 0px,
        var(--flag-white) 27px,
        var(--flag-red) 27px,
        var(--flag-red) 54px);
  }
  .flag-artwork::after {
    content: "";
    position: absolute;
    inset: 0;
    background: linear-gradient(90deg, rgba(127, 182, 201, 0.35) 0%, rgba(127, 182, 201, 0) 60%);
  }
  .title {
    position: absolute;
    margin: 0;
    font-family: "Alfa Slab One", serif;
    font-weight: 400;
    line-height: 1;
    letter-spacing: 1px;
    text-shadow: 4px 6px 6px var(--shadow);
  }
  .title-top {
    left: 77px;
    top: 58px;
    font-size: 104px;
    color: var(--title-red);
  }
  .title-bottom {
    left: 58px;
    top: 196px;
    font-size: 116px;
    color: var(--title-blue);
  }
</style>
</head>
<body>
  <main class="canvas">
    <section class="print">
      <div class="flag-artwork" role="img" aria-label="Weathered grunge American flag fading from light blue on the left into stars and red and white stripes on the right"></div>
      <h1 class="title title-top">COPPER</h1>
      <p class="title title-bottom">VALLEY</p>
    </section>
  </main>
</body>
</html>
```